Business Card Design

Freelance writer, coach, teacher and researcher specialising in improving mathematics teaching and learning in primary schools. I write books and articles for teachers, speak extensively at conferences in UK and aboard. Would like something with a cube in the design. Clean, modern - logo suitable for use on a website. Should NOT look 'childish' (no comic sans or chalkboard type fonts)

Full details to go on card:

Professor Dan Theroll
Unlocking Early Numeracy

info@dantheroll.net
#dantheroll26
www.dantheroll.net
+44 7812 660 394

Industry/Entity Type

Teacher

Contact Information for Business Card

Professor Dan Theroll
Unlocking Early Numbers

```html
<!DOCTYPE html>
<html lang="en">
<head>
<meta charset="UTF-8">
<title>Professor Dan Theroll — Business Card</title>
<link rel="stylesheet" href="https://fonts.googleapis.com/css2?family=Source+Sans+3:wght@400;600;700&display=swap">
<style>
  :root {
    --page-bg: #d6d7da;
    --card-bg: #ffffff;
    --card-edge: #3a3a3a;
    --edge-shade: #a9aaae;
    --ink: #111111;
    --brand-navy: #1d3f8f;
    --brand-blue: #2a5bb5;
    --icon-red: #b3191d;
    --deco-lavender: #c3c8e4;
    --deco-light: #e3e6f3;
  }
  * { margin: 0; padding: 0; box-sizing: border-box; }
  html, body {
    width: 1200px;
    height: 1200px;
    overflow: hidden;
    background: var(--page-bg);
    font-family: "Source Sans 3", "Myriad Pro", Arial, sans-serif;
  }
  .canvas {
    position: relative;
    width: 1200px;
    height: 1200px;
  }
  .business-card {
    position: absolute;
    left: 120px;
    top: 290px;
    width: 960px;
    height: 619px;
    background: var(--card-bg);
    border: 1px solid var(--card-edge);
    overflow: hidden;
  }
  .decor-field {
    position: absolute;
    left: 0;
    top: 92px;
    width: 434px;
    height: 527px;
    background: linear-gradient(160deg, var(--deco-light) 0%, var(--deco-lavender) 55%, #b9bfdf 100%);
  }
  .edge-shade {
    position: absolute;
    left: 0;
    top: 0;
    width: 118px;
    height: 100%;
    background: linear-gradient(to right, var(--edge-shade) 0%, #d4d5d8 45%, rgba(255,255,255,0) 100%);
  }
  .identity {
    position: absolute;
    left: 420px;
    top: 70px;
    display: flex;
    align-items: flex-start;
    gap: 22px;
  }
  .identity-mark {
    width: 30px;
    height: 30px;
    margin-top: 8px;
    background: var(--brand-navy);
  }
  .identity-name {
    font-size: 29px;
    font-weight: 700;
    line-height: 36px;
    color: var(--ink);
    letter-spacing: -0.2px;
  }
  .identity-tagline {
    font-size: 25px;
    font-weight: 400;
    line-height: 30px;
    color: var(--brand-blue);
  }
  .contact-list {
    position: absolute;
    left: 560px;
    top: 388px;
    list-style: none;
    font-size: 25px;
    line-height: 29px;
    color: var(--ink);
  }
  .contact-item {
    display: flex;
    align-items: center;
    gap: 10px;
    margin-bottom: 2px;
  }
  .contact-item.handle { margin-bottom: 6px; }
  .contact-icon {
    width: 26px;
    height: 26px;
    flex: 0 0 26px;
  }
  .contact-icon.blank { visibility: hidden; }
</style>
</head>
<body>
<main class="canvas">
  <section class="business-card" aria-label="Business card">
    <div class="decor-field" role="img" aria-label="Large faint decorative brand graphic in soft lavender"></div>
    <div class="edge-shade" aria-hidden="true"></div>

    <header class="identity">
      <div class="identity-mark" aria-hidden="true"></div>
      <div class="identity-text">
        <h1 class="identity-name">Professor Dan Theroll</h1>
        <p class="identity-tagline">Unlocking Early Numeracy</p>
      </div>
    </header>

    <ul class="contact-list">
      <li class="contact-item email">
        <svg class="contact-icon" viewBox="0 0 26 26" aria-hidden="true">
          <rect x="2" y="6" width="22" height="15" fill="var(--icon-red)"/>
          <polyline points="2,6 13,15 24,6" fill="none" stroke="#ffffff" stroke-width="1.8"/>
        </svg>
        <span>info@dantheroll.net</span>
      </li>
      <li class="contact-item handle">
        <span class="contact-icon blank" aria-hidden="true"></span>
        <span>#dantheroll26</span>
      </li>
      <li class="contact-item phone">
        <svg class="contact-icon" viewBox="0 0 26 26" aria-hidden="true">
          <path d="M6 4 L10 4 L11 9 L8.5 10.5 C10 14 12 16 15.5 17.5 L17 15 L22 16 L22 20 C22 21 21 22 20 22 C11 21 5 15 4 6 C4 5 5 4 6 4 Z" fill="var(--icon-red)"/>
        </svg>
        <span>+44 7812 660 394</span>
      </li>
      <li class="contact-item web">
        <svg class="contact-icon" viewBox="0 0 26 26" aria-hidden="true">
          <g fill="none" stroke="var(--icon-red)" stroke-width="2">
            <circle cx="13" cy="13" r="10"/>
            <ellipse cx="13" cy="13" rx="4.5" ry="10"/>
            <line x1="3" y1="13" x2="23" y2="13"/>
            <line x1="5" y1="7.5" x2="21" y2="7.5"/>
            <line x1="5" y1="18.5" x2="21" y2="18.5"/>
          </g>
        </svg>
        <span>www.dantheroll.net</span>
      </li>
    </ul>
  </section>
</main>
</body>
</html>
```